Flyer for the Radiant Harvest Worship Day

I am looking to create a flyer for a one day prayer retreat our church is organizing.
This flyer will be posted on social media, websites and will also be printed so it can be mailed to people.
I am looking for something professional, with good use of our logo and band colors (logo colors).
I am counting on the designer's skill, creativity, art and knowledge of media communication to produce a flyer that will effectively and quickly convey the message we are trying to spread.
CONTENT OF THE FLYER:
Event title: Radiant Harvest Worship Day
Date: Tuesday July 2nd, 2019
Time: 11:00AM - 7:00PM
Bellmont Hotel, 4815 Alder Lane, Portland, Maine 04117 (Room: Willowmere)
Event Key words to highlight what the event is about: Prayer, Sharing the Word, Panel discussion, prophecy, Impartation.
Key phrases:
A one day prayer retreat.
Jesus Chris is Lord
Contact info:
www.tovelin.org
Phone: 207 555 0193
Email: contact@brookhavenfold.org

```html
<!DOCTYPE html>
<html lang="en">
<head>
<meta charset="utf-8">
<title>Radiant Harvest Worship Day Flyer</title>
<link href="https://fonts.googleapis.com/css2?family=Poppins:wght@500;600;700&family=Roboto+Condensed:wght@700&display=swap" rel="stylesheet">
<style>
  :root {
    --stage: #5e5e5e;
    --ink-white: #ffffff;
    --accent-orange: #f7941d;
    --brand-navy: #0e3a63;
    --photo-black: #070707;
    --photo-dark: #1c1c1c;
    --photo-mid: #3e3e3e;
    --photo-soft: #6e6e6e;
    --photo-light: #b4b4b4;
  }
  * { margin: 0; padding: 0; box-sizing: border-box; }
  html, body {
    width: 1141px; height: 1200px; overflow: hidden;
    background: var(--stage);
    font-family: "Poppins", sans-serif;
  }
  .flyer {
    position: absolute;
    left: 219px; top: 100px;
    width: 703px; height: 999px;
    overflow: hidden;
    color: var(--ink-white);
  }
  .flyer__photo {
    position: absolute; inset: 0;
    background:
      radial-gradient(ellipse 34% 22% at 55% 30%, rgba(150,150,150,0.45), rgba(0,0,0,0) 100%),
      radial-gradient(ellipse 30% 45% at 22% 62%, rgba(170,170,170,0.35), rgba(0,0,0,0) 100%),
      radial-gradient(ellipse 28% 40% at 46% 58%, rgba(190,190,190,0.30), rgba(0,0,0,0) 100%),
      radial-gradient(ellipse 45% 30% at 80% 88%, rgba(210,210,210,0.45), rgba(0,0,0,0) 100%),
      radial-gradient(ellipse 40% 30% at 18% 95%, rgba(150,150,150,0.40), rgba(0,0,0,0) 100%),
      linear-gradient(180deg, var(--photo-black) 0%, var(--photo-dark) 22%, var(--photo-mid) 48%, var(--photo-soft) 72%, var(--photo-light) 100%);
  }
  .keywords {
    position: absolute; top: 59px; left: 0; width: 100%;
    text-align: center;
    font-size: 17.5px; font-weight: 500; letter-spacing: 0.1px;
  }
  .keywords .sep { color: var(--accent-orange); margin: 0 7px; }
  .title-frame {
    position: absolute; left: 107px; top: 133px;
    width: 488px; height: 176px;
    border: 1.5px solid var(--accent-orange);
  }
  .title-box {
    position: absolute; left: 116px; top: 142px;
    width: 470px; height: 159px;
    background: var(--accent-orange);
    display: flex; align-items: center; justify-content: center;
  }
  .title {
    font-family: "Roboto Condensed", sans-serif;
    font-weight: 700; font-size: 62px; line-height: 64px;
    text-align: center; letter-spacing: -0.5px;
  }
  .event-when {
    position: absolute; top: 318px; left: 0; width: 100%;
    text-align: center; font-size: 16.5px; font-weight: 600;
  }
  .brand-mark {
    position: absolute; left: 277px; top: 731px;
    width: 147px; height: 147px;
    background: var(--brand-navy);
    display: flex; align-items: center; justify-content: center;
  }
  .brand-mark__name {
    font-size: 30px; font-weight: 600; color: var(--ink-white);
  }
  .venue {
    position: absolute; top: 895px; left: 0; width: 100%;
    text-align: center; font-size: 14px; font-weight: 600; line-height: 16px;
  }
  .contact {
    position: absolute; top: 940px; left: 0; width: 100%;
    text-align: center; font-size: 12px; font-weight: 600;
  }
  .contact .sep { margin: 0 9px; }
  .web-band {
    position: absolute; left: 0; bottom: 0;
    width: 100%; height: 23px;
    background: var(--brand-navy);
    display: flex; align-items: center; justify-content: center;
    font-size: 12px; font-weight: 600;
  }
</style>
</head>
<body>
  <main class="flyer">
    <div class="flyer__photo" role="img" aria-label="Black and white photo of a worship congregation raising their hands in prayer"></div>

    <p class="keywords">Prayer<span class="sep">|</span>Sharing the Word<span class="sep">|</span>Panel Discussion<span class="sep">|</span>Prophecy<span class="sep">|</span>Impartation</p>

    <div class="title-frame"></div>
    <div class="title-box">
      <h1 class="title">Radiant Harvest<br>Worship Day</h1>
    </div>

    <p class="event-when">Date: Tuesday July 2nd, 2019 &nbsp;|&nbsp; Time: 11:00AM - 7:00PM</p>

    <div class="brand-mark">
      <span class="brand-mark__name">Tovelin</span>
    </div>

    <p class="venue">Venue:<br>Bellmont Hotel, 4815 Alder Lane, Portland, Maine 04117 (Room: Willowmere)</p>

    <p class="contact">Phone: 207 555 0193<span class="sep">|</span>Email: contact@brookhavenfold.org</p>

    <footer class="web-band">www.tovelin.org</footer>
  </main>
</body>
</html>
```